Most captivating card ever!

Life Coach - Professional Adventurer - Entrepreneur
I need the worlds most amazing business card for my personal brand. This business card will mostly be used to give to prospective clients for life coaching and business coaching.
Be creative, be adventurous. It needs to stand out. Make people say.. I need this guy!
My background is as an entrepreneur and professional adventurer undertaking extreme expeditions. I am now moving into life coaching.
No specific design ideas, so you have full creativity. Show me your best.
Industry/Entity Type
Life Coaching
Contact Information for Business Card
Dan Pellow
itsdanp.com.au
0468215903
Colors
Designer to choose colors to be used in the design.
Look and feel

```html
<!DOCTYPE html>
<html lang="en">
<head>
<meta charset="utf-8">
<title>Dan Pellow – Business Card</title>
<link rel="stylesheet" href="https://fonts.googleapis.com/css2?family=Nunito:wght@400;500&display=swap">
<style>
  :root {
    --page-bg: #ffffff;
    --card-bg: #ffffff;
    --brand-red: #ed1c24;
    --ink: #111111;
    --edge: #e6e6e6;
  }
  html, body {
    margin: 0;
    padding: 0;
    width: 1200px;
    height: 1000px;
    overflow: hidden;
    background: var(--page-bg);
    font-family: "Nunito", Arial, sans-serif;
  }
  .canvas {
    position: relative;
    width: 1200px;
    height: 1000px;
  }
  .card {
    position: absolute;
    left: 235px;
    top: 292px;
    width: 730px;
    height: 416px;
    background: var(--card-bg);
    outline: 1px solid var(--edge);
    overflow: hidden;
  }
  .brand-mark {
    position: absolute;
    left: 49px;
    top: 59px;
    width: 136px;
    height: 136px;
    border-radius: 50%;
    background: radial-gradient(circle, rgba(237,28,36,0.08) 0%, rgba(237,28,36,0.35) 70%, rgba(237,28,36,0.15) 100%);
  }
  .identity {
    position: absolute;
    left: 52px;
    top: 205px;
  }
  .name {
    margin: 0;
    font-size: 40px;
    font-weight: 500;
    line-height: 48px;
    color: var(--brand-red);
    letter-spacing: 0.2px;
  }
  .roles {
    margin: 8px 0 0;
    font-size: 19px;
    line-height: 29px;
    color: var(--ink);
  }
  .contact {
    margin: 0;
    font-size: 19px;
    line-height: 29px;
    color: var(--brand-red);
  }
  .footer-band {
    position: absolute;
    left: 0;
    bottom: 0;
    width: 100%;
    height: 22px;
    background: var(--brand-red);
  }
</style>
</head>
<body>
  <main class="canvas">
    <section class="card">
      <div class="brand-mark" role="img" aria-label="Red brush-stroke circle emblem"></div>
      <div class="identity">
        <h1 class="name">Dan Pellow</h1>
        <p class="roles">Life Coach - Professional Adventurer - Entrepreneur</p>
        <p class="contact website">itsdanp.com.au</p>
        <p class="contact phone">0468215903</p>
      </div>
      <div class="footer-band"></div>
    </section>
  </main>
</body>
</html>
```